Business Card Design

A logo and business card design is required for a new podiatry business based on the Great Ocean Road, Victoria, Australia. The business will provide broad array of podiatry services to communities along the coast.

A distinctive design is sought that represents both professional allied health service delivery and the iconic location of the service, where the ocean meets the Otway ranges. Colours representative of the ocean blues, greens of the local forrest would be desirable.

Target Market(s)

GP's, other allied health professionals, members of the community with foot complaints

Industry/Entity Type

Health

Contact Information for Business Card

Tidewater Bend Podiatry
Gareth Linwell
B.Pod B App Sci (HM)
Phone: 0400 718 306
Email: tidewaterbendpodiatry@mailbrook.net

Requirements
Must have
• On the back of the card room allocated for appointment times.
Nice to have
• Would like the logo to incorporate a foot and the elements of the coast, whether it be ocean &/or the unique elements of the coast and the great ocean road.

```html
<!DOCTYPE html>
<html lang="en">
<head>
<meta charset="utf-8">
<title>Tidewater Bend Podiatry – Business Card</title>
<link rel="stylesheet" href="https://fonts.googleapis.com/css2?family=Open+Sans:wght@400;700&family=Lobster&display=swap">
<style>
  :root {
    --ocean: #6ccbdb;
    --navy: #2a3592;
    --paper: #ffffff;
    --backdrop: #e9e6e2;
    --sun: #f3c431;
  }
  * { box-sizing: border-box; margin: 0; padding: 0; }
  html, body { width: 1200px; height: 865px; overflow: hidden; }
  body {
    background: var(--backdrop);
    font-family: "Open Sans", Arial, sans-serif;
    color: var(--navy);
    display: flex;
    flex-direction: column;
    align-items: center;
    justify-content: center;
    gap: 40px;
  }
  .card {
    position: relative;
    width: 620px;
    height: 379px;
    box-shadow: 0 4px 14px rgba(0,0,0,.18);
  }
  .card--front { background: var(--ocean); }
  .card--back { background: var(--paper); }

  .brand {
    position: absolute;
    display: flex;
    align-items: center;
    gap: 10px;
    font-weight: 700;
    color: var(--navy);
    line-height: 1.1;
  }
  .brand__dot {
    width: 30px; height: 30px;
    border-radius: 50%;
    background: var(--sun);
    flex: none;
  }
  .card--front .brand { left: 28px; top: 26px; font-size: 20px; width: 210px; }

  .practitioner {
    position: absolute;
    right: 30px; top: 60px;
    text-align: right;
    font-weight: 700;
    font-size: 22px;
    line-height: 1.15;
  }
  .contact {
    position: absolute;
    left: 0; right: 0;
    text-align: center;
    font-size: 24px;
  }
  .contact svg { display: block; margin: 0 auto 4px; }
  .contact--phone { top: 140px; }
  .contact--email { top: 230px; font-size: 23px; }

  .appointment__title {
    position: absolute;
    top: 26px; left: 0; right: 0;
    text-align: center;
    font-family: "Lobster", cursive;
    font-size: 28px;
  }
  .field {
    position: absolute;
    display: flex;
    align-items: flex-end;
    font-family: "Lobster", cursive;
    font-size: 28px;
  }
  .field__line {
    flex: 1;
    border-bottom: 3px solid var(--navy);
    margin-left: 6px;
    height: 26px;
  }
  .field--name { left: 30px; top: 80px; width: 560px; }
  .field--date { left: 30px; top: 150px; width: 270px; }
  .field--time { left: 330px; top: 215px; width: 260px; }

  .card--back .brand { right: 30px; top: 270px; font-size: 17px; width: 200px; }
  .back-phone {
    position: absolute;
    right: 30px; top: 312px;
    font-size: 22px;
  }
  .back-email {
    position: absolute;
    left: 30px; bottom: 18px;
    font-size: 20px;
  }
</style>
</head>
<body>
  <section class="card card--front" aria-label="Card front">
    <div class="brand"><span class="brand__dot"></span><span>Tidewater Bend Podiatry</span></div>
    <div class="practitioner">
      <div>Gareth Linwell</div>
      <div>B.Pod B App Sci (HM)</div>
    </div>
    <div class="contact contact--phone">
      <svg width="40" height="30" viewBox="0 0 40 30" aria-hidden="true">
        <path d="M3 10 Q20 0 37 10 L34 14 L27 12 L26 8 Q20 6 14 8 L13 12 L6 14 Z" fill="var(--navy)"/>
        <path d="M12 13 L28 13 L34 27 L6 27 Z" fill="var(--navy)"/>
        <circle cx="20" cy="20" r="4" fill="var(--ocean)"/>
      </svg>
      0400 718 306
    </div>
    <div class="contact contact--email">
      <svg width="44" height="30" viewBox="0 0 44 30" aria-hidden="true">
        <rect x="2" y="2" width="40" height="26" fill="none" stroke="var(--navy)" stroke-width="3"/>
        <path d="M2 2 L22 18 L42 2 M2 28 L17 14 M42 28 L27 14" fill="none" stroke="var(--navy)" stroke-width="3"/>
      </svg>
      tidewaterbendpodiatry@mailbrook.net
    </div>
  </section>

  <section class="card card--back" aria-label="Card back">
    <div class="appointment__title">Appointment</div>
    <div class="field field--name">Name:<span class="field__line"></span></div>
    <div class="field field--date">Date:<span class="field__line"></span></div>
    <div class="field field--time">Time:<span class="field__line"></span></div>
    <div class="brand"><span class="brand__dot"></span><span>Tidewater Bend Podiatry</span></div>
    <div class="back-phone">0400 718 306</div>
    <div class="back-email">tidewaterbendpodiatry@mailbrook.net</div>
  </section>
</body>
</html>
```